I need creative and unique business card design using my company logo. Ok to change logo color. We are a small brokerage doing both Real Estate and Mortgage services. Need to have the follow on business card;
1. agent name - Nora Velden - Realtor
2. cell - 211-555-0182
3. license number - DRE 07164392
4. business name - Bright Keys & Lending, Inc
5. business office - 411-555-0147
6. business address - 214 W. Marlowe Ave #308, Larkmoor CA 90999
7. business logo - attached (ok to use different color on logo)

```html
<!DOCTYPE html>
<html lang="en">
<head>
<meta charset="utf-8">
<title>Bright Keys &amp; Lending – Business Card</title>
<link rel="stylesheet" href="https://fonts.googleapis.com/css2?family=Open+Sans:wght@400;600;700&display=swap">
<style>
  :root {
    --backdrop: #222222;
    --card: #1e1f24;
    --card-edge: #17181c;
    --decor: #252a33;
    --blue: #0a8fe0;
    --blue-deep: #1e5bbf;
    --white: #f2f4f7;
  }
  * { box-sizing: border-box; margin: 0; padding: 0; }
  html, body {
    width: 1200px; height: 780px; overflow: hidden;
    background: var(--backdrop);
    font-family: "Open Sans", Arial, sans-serif;
  }
  .sheet {
    width: 1200px; height: 780px;
    display: flex; align-items: center; justify-content: center; gap: 40px;
  }
  .card {
    position: relative;
    width: 560px; height: 340px;
    background: var(--card);
    overflow: hidden;
    box-shadow: 0 18px 40px rgba(0,0,0,.45), 0 0 0 1px var(--card-edge);
  }

  /* front */
  .decor-panel {
    position: absolute; left: 300px; top: 150px;
    width: 260px; height: 190px;
    background: linear-gradient(135deg, var(--card) 0%, var(--decor) 100%);
  }
  .brand {
    position: absolute; left: 70px; top: 40px;
    display: flex; align-items: center; gap: 12px;
  }
  .brand-mark { width: 26px; height: 26px; background: var(--blue-deep); flex: none; }
  .brand-name {
    color: var(--blue-deep); font-weight: 600; font-size: 15px;
    letter-spacing: .12em; text-transform: uppercase;
  }
  .address {
    position: absolute; left: 40px; top: 112px;
    color: var(--white); font-size: 14px; line-height: 1.45;
  }
  .phones {
    position: absolute; left: 24px; top: 172px;
    list-style: none; color: var(--white); font-size: 14px; line-height: 1.5;
  }
  .phones li { display: flex; align-items: center; gap: 8px; }
  .phones svg { width: 12px; height: 12px; flex: none; }
  .agent {
    position: absolute; right: 70px; top: 176px; text-align: right;
  }
  .agent-name {
    color: var(--blue); font-weight: 700; font-size: 36px; line-height: 1.1;
  }
  .agent-title { color: var(--white); font-size: 18px; font-weight: 600; line-height: 1.2; }
  .accent-tab {
    position: absolute; right: 30px; top: 230px;
    width: 34px; height: 44px;
    background: linear-gradient(90deg, var(--blue-deep), var(--blue));
  }
  .license {
    position: absolute; left: 268px; bottom: 24px;
    color: var(--white); font-size: 19px; font-weight: 600;
  }
  .license-label { color: var(--blue); font-weight: 400; }

  /* back */
  .card-back { display: flex; align-items: center; justify-content: center; }
  .back-brand { display: flex; align-items: center; gap: 16px; }
  .back-brand .brand-mark { width: 40px; height: 40px; }
  .back-brand .brand-name { font-size: 20px; }
</style>
</head>
<body>
<main class="sheet">
  <section class="card card-front">
    <div class="decor-panel" aria-hidden="true"></div>
    <div class="brand">
      <span class="brand-mark"></span>
      <span class="brand-name">Bright Keys &amp; Lending, Inc</span>
    </div>
    <p class="address">214 W. Marlowe Ave #308,<br>Larkmoor CA 90999</p>
    <ul class="phones">
      <li>
        <svg viewBox="0 0 12 12" aria-hidden="true"><rect x="3" y="0.5" width="6" height="11" rx="1" fill="none" stroke="var(--blue)" stroke-width="1.2"/></svg>
        211-555-0182
      </li>
      <li>
        <svg viewBox="0 0 12 12" aria-hidden="true"><path d="M2.5 1 L4.5 1 L5.2 3.6 L3.9 4.6 Q5 7 7.4 8.1 L8.4 6.8 L11 7.5 L11 9.5 Q11 11 9.5 11 Q1 10 1 2.5 Q1 1 2.5 1 Z" fill="var(--blue)"/></svg>
        411-555-0147
      </li>
    </ul>
    <div class="agent">
      <h1 class="agent-name">Nora Velden</h1>
      <p class="agent-title">Realtor</p>
    </div>
    <span class="accent-tab"></span>
    <p class="license"><span class="license-label">DRE</span> 07164392</p>
  </section>

  <section class="card card-back">
    <div class="back-brand">
      <span class="brand-mark"></span>
      <span class="brand-name">Bright Keys &amp; Lending, Inc</span>
    </div>
  </section>
</main>
</body>
</html>
```